Brookfern Sack operates across the US and Australasia providing calico bags to small business through to large enterprise across all verticals. Our bags are the most premium in the market place and our customer service is second to none. Our competitive advantage lays in our competitive pricing, superior quality and outstanding customer service.

Industry/Entity Type

Business

Contact Information for Business Card

Brookfern Sack
Miriam Tolvesk
Managing Director
miriam@brookfernsack.example
www.brookfernsack.example.au
Mobile:- 0491 607 385
Level 3, 248 Harwick Street
Melbourne Victoria Australia 3999

```html
<!DOCTYPE html>
<html lang="en">
<head>
<meta charset="utf-8">
<title>Brookfern Sack – Business Card</title>
<link href="https://fonts.googleapis.com/css2?family=Noto+Sans:wght@400;600&family=Roboto:wght@500;700&display=swap" rel="stylesheet">
<style>
  :root {
    --backdrop: #cbcbcb;
    --card: #f6f6f6;
    --brand-green: #4f8a1b;
    --leaf-green: #6cbf2a;
    --brand-red: #d0101e;
    --ink: #1e1e1e;
    --photo-light: #f2f1ee;
    --photo-mid: #e4e2dc;
  }
  * { box-sizing: border-box; margin: 0; padding: 0; }
  html, body { width: 1200px; height: 1005px; overflow: hidden; }
  body {
    background: var(--backdrop);
    font-family: "Noto Sans", sans-serif;
    color: var(--ink);
    position: relative;
  }
  .card {
    position: absolute;
    left: 260px;
    width: 680px;
    height: 400px;
    background: var(--card);
    box-shadow: 0 6px 18px rgba(0,0,0,0.22);
    overflow: hidden;
  }
  .card--front { top: 80px; }
  .card--back { top: 525px; }

  .front-photo {
    position: absolute; inset: 0;
    background:
      radial-gradient(ellipse at 30% 55%, var(--photo-mid) 0%, transparent 55%),
      radial-gradient(ellipse at 75% 60%, #ebe9e4 0%, transparent 60%),
      linear-gradient(180deg, #f7f7f6 0%, var(--photo-light) 60%, #e9e6e0 100%);
  }
  .front-brand {
    position: absolute; inset: 0;
    display: flex; align-items: center; justify-content: center; gap: 16px;
  }
  .brand-dot {
    width: 34px; height: 34px; border-radius: 50%;
    background: var(--leaf-green);
  }
  .brand-name {
    font-family: "Roboto", sans-serif;
    font-weight: 700;
    color: var(--brand-green);
    letter-spacing: 0.5px;
  }
  .front-brand .brand-name { font-size: 44px; }

  .back-brand {
    position: absolute; left: 40px; top: 88px;
    display: flex; align-items: center; gap: 12px;
  }
  .back-brand .brand-dot { width: 24px; height: 24px; }
  .back-brand .brand-name { font-size: 30px; }

  .person { position: absolute; left: 40px; top: 262px; }
  .person-name {
    font-family: "Roboto", sans-serif;
    font-weight: 700; font-size: 27px;
    color: var(--brand-green);
  }
  .person-title { font-size: 15px; margin-top: 2px; }

  .contact {
    position: absolute; left: 355px; top: 150px;
    font-size: 16px; line-height: 26px;
    list-style: none;
  }
  .contact li { display: flex; align-items: center; gap: 12px; }
  .contact svg { width: 15px; height: 15px; fill: var(--brand-green); flex: none; }
  .contact .address { padding-left: 0; }

  .footer-bands { position: absolute; left: 0; bottom: 0; width: 680px; height: 32px; }
</style>
</head>
<body>
  <section class="card card--front" aria-label="Card front">
    <div class="front-photo" role="img" aria-label="Soft faded photograph of white calico drawstring bags in a wire basket"></div>
    <div class="front-brand">
      <span class="brand-dot"></span>
      <span class="brand-name">Brookfern Sack</span>
    </div>
  </section>

  <section class="card card--back" aria-label="Card back">
    <div class="back-brand">
      <span class="brand-dot"></span>
      <span class="brand-name">Brookfern Sack</span>
    </div>

    <div class="person">
      <p class="person-name">Miriam Tolvesk</p>
      <p class="person-title">Managing Director</p>
    </div>

    <ul class="contact">
      <li>
        <svg viewBox="0 0 16 16" aria-hidden="true"><path d="M2 5c0-2 2-3 6-3s6 1 6 3v1h-3V5H5v1H2z M4 7h8l2 6H2z"/></svg>
        0491 607 385
      </li>
      <li>
        <svg viewBox="0 0 16 16" aria-hidden="true"><path d="M1 3h14v10H1z M2 4l6 5 6-5" stroke="#f6f6f6" stroke-width="1"/></svg>
        miriam@brookfernsack.example
      </li>
      <li>
        <svg viewBox="0 0 16 16" aria-hidden="true"><circle cx="8" cy="8" r="7"/><path d="M1 8h14M8 1c-3 3-3 11 0 14M8 1c3 3 3 11 0 14" stroke="#f6f6f6" stroke-width="1" fill="none"/></svg>
        www.brookfernsack.example.au
      </li>
      <li class="address">Level 3, 248 Harwick Street</li>
      <li class="address">Melbourne Victoria Australia 3999</li>
    </ul>

    <svg class="footer-bands" viewBox="0 0 680 32" aria-hidden="true">
      <polygon points="0,18 472,18 458,32 0,32" fill="var(--brand-green)"/>
      <polygon points="484,14 680,0 680,14 470,32 466,32 484,18" fill="var(--brand-red)"/>
    </svg>
  </section>
</body>
</html>
```